Brand Rosalind Seashell (Roller Facial Roller product designs and clear instructions)

Hello all you beautiful mermaids and mermaid lovers alike,
We are a family run business selling facial rollers in the health and beauty niche, The branding/logo is considered feminine, creative and overall inspired by mythology styled mermaids. We hope to attract a wide range of health and beauty lovers, an audience whom adore an unique luxury to add to their natural beauty and skin care regime collection. (whilst feeling like the beautiful mermaids they they are inside!)

To scale things up a notch and add a personal touch we need thank you inserts with our logo/branding on it for promotional purpose, customer guidance and satisfaction are very important to us. These thank you inserts will give confidence for our customers to feel free to contact by Email or write a product review at their convenience. We also require an illustration with clear instructions on how to use a facial roller in our brand style and colors.
We need art work and our branding information for the back of our box packaging

Please see attachments of our brand logo design, I have drawn a basic example template for the illustration instructions for facial roller use but will provide more depth of details as required, also the mermaid aquatic art theme for the back of our box packaging and color scheme is provided.

Regards,
Rosalind Seashell

Target Market(s)

Beauty and health

Font styles to use
Decorative
Script

Colors
34a7d7
85cae6
00a990
33b8a4
1f68ad
b7a5cd
886aae
6b449b
50c0af

Requirements
Must have
• My project must have eye catching beauty and be as similar as possible to my attached art designs but a lot more professional looking overall.
Must include ''Thank YOU you are a true mermaid. Here at Rosalind Seashell we are a family run business and your purchase and reviews mean a lot for our beautiful mermaids satisfaction, don't be shy to contact us at rosalindseashell@mailbox-example.com if there are any inquiries. We hope that this facial roller will be a gem added to your natural health and beauty collection. Unleashing your inner and outer mermaid beauty by rejuvenation. ''
Colors must be consistent shades of purple, green and blue and other aquatic cool tones, black and white is completely fine were applicable.
Must have illustration instructions of how to use a facial roller correctly and safety (see attachments for reference) However must have long purple hair like a mermaid as this will help the brand stand out for it's unique attention to detail.
Nice to have
• Anything fun and bright. Creative imagination, love of mermaids and mythological inspired art for branding .
Should not have
• My project must not have anything boring or dull. This is an exciting project and Rosalind Seashell is all about fun, self love and natural beauty.

DO NOT NEED TO CHANGE THE BRAND LOGO only need facial roller illustration instructions, mermaid inspired Thank you card inserts for the box packaging for customer satifcation , thank you!

```html
<!DOCTYPE html>
<html lang="en">
<head>
<meta charset="utf-8">
<title>Thank You Insert – Rosalind Seashell</title>
<link rel="stylesheet" href="https://fonts.googleapis.com/css2?family=Allison&family=Quicksand:wght@400&display=swap">
<style>
  :root {
    --stage: #333333;
    --ink: #111111;
    --sky-deep: #6a9fee;
    --sky-mid: #8fb8f1;
    --sky-pale: #cfe0f8;
    --paper: #ffffff;
    --teal: #2f8f8a;
    --sea-green: #3a9a93;
    --ocean: #2a62b0;
    --navy: #1d4a8a;
    --violet: #6b449b;
    --splash: #3f6fd0;
  }
  * { box-sizing: border-box; margin: 0; padding: 0; }
  html, body {
    width: 1200px;
    height: 1000px;
    overflow: hidden;
    background: var(--stage);
  }
  .insert-card {
    position: absolute;
    left: 187px;
    top: 221px;
    width: 784px;
    height: 580px;
    overflow: hidden;
    background:
      radial-gradient(ellipse at 20% 10%, rgba(255,255,255,0.18), transparent 45%),
      linear-gradient(180deg, var(--sky-deep) 0%, var(--sky-mid) 38%, var(--sky-pale) 70%, var(--paper) 92%);
  }
  .insert-title {
    position: absolute;
    left: 36px;
    top: -14px;
    font-family: "Allison", cursive;
    font-weight: 400;
    font-size: 118px;
    line-height: 1.1;
    color: var(--ink);
    white-space: nowrap;
  }
  .insert-message {
    position: absolute;
    left: 7px;
    top: 117px;
    font-family: "Quicksand", sans-serif;
    font-weight: 400;
    font-size: 26.5px;
    line-height: 34.6px;
    letter-spacing: 1.5px;
    color: var(--ink);
  }
  .insert-message span {
    display: block;
    white-space: nowrap;
  }
  .insert-message .contact-email {
    letter-spacing: 0;
  }
  .art-splash {
    position: absolute;
    left: 508px;
    top: 20px;
    width: 272px;
    height: 545px;
    border-radius: 45% 55% 40% 50% / 30% 35% 40% 45%;
    background: radial-gradient(ellipse at 55% 55%, rgba(63,111,208,0.55) 0%, rgba(63,111,208,0.25) 55%, rgba(63,111,208,0) 75%);
  }
  .mermaid-art {
    position: absolute;
    left: 535px;
    top: 16px;
    width: 225px;
    height: 545px;
    border-radius: 90px 90px 30px 30px / 110px 110px 30px 30px;
    background:
      radial-gradient(ellipse 55% 28% at 72% 22%, var(--violet) 0%, rgba(107,68,155,0.7) 50%, rgba(107,68,155,0) 100%),
      linear-gradient(90deg, var(--sea-green) 0%, var(--teal) 35%, var(--ocean) 65%, rgba(42,98,176,0.85) 100%),
      linear-gradient(180deg, var(--teal) 0%, var(--navy) 100%);
    background-blend-mode: normal, multiply, normal;
    opacity: 0.92;
  }
</style>
</head>
<body>
  <main class="insert-card">
    <h1 class="insert-title">Thank You</h1>
    <p class="insert-message">
      <span>You are a true mermaid. Here at</span>
      <span>Rosalind Seashell we are a family</span>
      <span>run business and your purchase</span>
      <span>and reviews mean a lot for our</span>
      <span>beautiful mermaids satisfaction,</span>
      <span>don't be shy to contact us at</span>
      <span class="contact-email">rosalindseashell@mailbox-example.com</span>
      <span>if there are any inquiries. We hope</span>
      <span>that this facial roller will be a gem</span>
      <span>added to your natural health and</span>
      <span>beauty collection. Unleashing your</span>
      <span>inner and outer mermaid beauty by</span>
      <span>rejuvenation.</span>
    </p>
    <div class="art-splash" aria-hidden="true"></div>
    <div class="mermaid-art" role="img" aria-label="Watercolour illustration of a mermaid seen from behind, with long purple hair and a blue-green tail on a blue paint splash"></div>
  </main>
</body>
</html>
```